Brexmoor Solutions
Not Necessary
Simple
Marlon Teague
N/A
marlon@brexmoorsolutions.example
http://www.brexmoorsolutions.example
Brexmoor Solutions is a custom development/software development firm. Specialize on web and mobile development.
I'd be interested in what a double sided business card looks like but may settle on a one-sided card.
Your discretion on whether to use logo's font or another - whatever looks best.
Logo and fonts

```html
<!DOCTYPE html>
<html lang="en">
<head>
<meta charset="utf-8">
<title>Brexmoor Solutions – Business Card</title>
<link href="https://fonts.googleapis.com/css2?family=Open+Sans:wght@400;600;700&display=swap" rel="stylesheet">
<style>
  :root {
    --backdrop: #2b2b2b;
    --card-white: #ffffff;
    --brand-blue: #1f6fae;
    --blue-deep: #0e4f8a;
    --blue-light: #3b8ccc;
    --swoosh-grey: #c9cdd2;
    --text-white: #ffffff;
    --text-soft: #d9e8f5;
  }
  * { margin: 0; padding: 0; box-sizing: border-box; }
  html, body {
    width: 1200px; height: 780px; overflow: hidden;
    background: var(--backdrop);
    font-family: "Open Sans", Arial, sans-serif;
  }
  .canvas {
    position: relative; width: 1200px; height: 780px;
    display: flex; align-items: center; justify-content: center;
  }
  .business-card {
    position: relative; width: 1000px; height: 572px;
    background: var(--card-white);
    border-radius: 30px; overflow: hidden;
  }
  .card-waves {
    position: absolute; inset: 0; width: 100%; height: 100%;
  }
  .brand-name {
    position: absolute; left: 120px; top: 110px;
    font-size: 76px; font-weight: 600; letter-spacing: 1px;
    color: var(--brand-blue); line-height: 1;
  }
  .holder {
    position: absolute; left: 190px; top: 388px; text-align: right; width: 230px;
    color: var(--text-white);
  }
  .holder-name { font-size: 30px; font-weight: 700; }
  .holder-title { font-size: 19px; color: var(--text-soft); margin-top: 6px; }
  .divider {
    position: absolute; left: 458px; top: 370px; width: 2px; height: 130px;
    background: var(--text-soft); opacity: .8;
  }
  .contact-list {
    position: absolute; left: 482px; top: 370px; list-style: none;
    color: var(--text-white); font-size: 19px;
  }
  .contact-list li { display: flex; align-items: center; height: 42px; }
  .contact-icon { width: 22px; height: 22px; margin-right: 14px; flex: none; }
</style>
</head>
<body>
<div class="canvas">
  <div class="business-card">
    <svg class="card-waves" viewBox="0 0 1000 572" preserveAspectRatio="none" aria-hidden="true">
      <defs>
        <linearGradient id="bandBlue" x1="0" y1="0" x2="1" y2="1">
          <stop offset="0" stop-color="var(--blue-light)"/>
          <stop offset="0.5" stop-color="var(--brand-blue)"/>
          <stop offset="1" stop-color="var(--blue-deep)"/>
        </linearGradient>
      </defs>
      <path d="M0 318 C 260 300, 520 330, 740 280 C 860 252, 940 215, 1000 190 L1000 220 C 930 250, 850 290, 740 305 C 520 340, 260 320, 0 340 Z" fill="var(--swoosh-grey)"/>
      <path d="M0 345 C 260 325, 520 350, 740 310 C 860 288, 940 250, 1000 225 L1000 572 L0 572 Z" fill="url(#bandBlue)"/>
    </svg>

    <div class="brand-name">Brexmoor Solutions</div>

    <div class="holder">
      <div class="holder-name">Marlon Teague</div>
      <div class="holder-title">N/A</div>
    </div>

    <div class="divider"></div>

    <ul class="contact-list">
      <li>
        <svg class="contact-icon" viewBox="0 0 24 24" aria-hidden="true"><rect x="6" y="2" width="12" height="20" rx="2" fill="none" stroke="#fff" stroke-width="2"/><circle cx="12" cy="18" r="1.3" fill="#fff"/></svg>
        555-014-2287
      </li>
      <li>
        <svg class="contact-icon" viewBox="0 0 24 24" aria-hidden="true"><rect x="2" y="5" width="20" height="14" rx="2" fill="none" stroke="#fff" stroke-width="2"/><path d="M3 6 L12 13 L21 6" fill="none" stroke="#fff" stroke-width="2"/></svg>
        marlon@brexmoorsolutions.example
      </li>
      <li>
        <svg class="contact-icon" viewBox="0 0 24 24" aria-hidden="true"><circle cx="12" cy="12" r="9.5" fill="none" stroke="#fff" stroke-width="2"/><ellipse cx="12" cy="12" rx="4" ry="9.5" fill="none" stroke="#fff" stroke-width="1.6"/><path d="M2.5 12 H21.5" stroke="#fff" stroke-width="1.6"/></svg>
        www.brexmoorsolutions.example
      </li>
    </ul>
  </div>
</div>
</body>
</html>
```